Golden Crust Supper Invitation

We will be having a Fish Fry on May 17th from 6PM -10PM. Location is 4721 Quillon Ln. Mansfield, TX 76048. We need a Invitation, which includes a the header reading "Golden Crust Supper". Wording of "Golden Crust Supper" should incorporate both baseball and food batter. Think baseball bats dripping in batter. Admission to all you can eat fish fry will be a donation of any baseball equipment including: bats, gloves, jerseys, cleats, balls, or financial donation. Proceeds will go towards funding Pemberly Family in traveling to Dominican Republic to conduct baseball ministries. It would great to incorporate Dominican Republic flag or colors.

```html
<!DOCTYPE html>
<html lang="en">
<head>
<meta charset="utf-8">
<title>Golden Crust Supper Invitation</title>
<link rel="stylesheet" href="https://fonts.googleapis.com/css2?family=Bebas+Neue&family=Roboto:wght@400;700&display=swap">
<style>
  :root {
    --red: #ed1c29;
    --navy: #1a3160;
    --white: #ffffff;
    --backdrop: #808285;
  }
  html, body {
    margin: 0;
    padding: 0;
    width: 965px;
    height: 1200px;
    overflow: hidden;
    background: var(--backdrop);
  }
  .invitation {
    position: absolute;
    left: 82px;
    top: 82px;
    width: 800px;
    height: 1035px;
    display: block;
  }
  .display { font-family: "Bebas Neue", "Oswald", sans-serif; }
  .body-text { font-family: "Roboto", Arial, sans-serif; }
  .navy { fill: var(--navy); }
  .red { fill: var(--red); }
  .white { fill: var(--white); }
</style>
</head>
<body>
<svg class="invitation" viewBox="131 131 1276 1650" xmlns="http://www.w3.org/2000/svg" aria-labelledby="invite-title">
  <title id="invite-title">Golden Crust Supper all-you-can-eat fish fry invitation</title>

  <!-- Sheet -->
  <rect class="white" x="131" y="131" width="1276" height="1650"/>

  <!-- Header bands -->
  <g class="header-bands">
    <polygon class="red" points="131,131 1407,131 1407,170 770,332 131,170"/>
    <polygon class="navy" points="131,190 770,352 1407,190 1407,255 770,405 131,255"/>
    <polygon class="navy" points="131,275 380,340 131,425"/>
    <polygon class="red" points="1407,275 1160,345 1407,425"/>
  </g>

  <!-- Event name mark -->
  <g class="event-mark">
    <rect class="white" x="600" y="290" width="340" height="110"/>
    <text class="display navy" x="770" y="368" font-size="64" text-anchor="middle" textLength="300" lengthAdjust="spacingAndGlyphs">GOLDEN CRUST SUPPER</text>
  </g>

  <!-- Fish illustrations -->
  <rect class="red" x="178" y="382" width="352" height="166" role="img" aria-label="Illustration of a red fish swimming right"/>
  <rect class="navy" x="1012" y="382" width="352" height="166" role="img" aria-label="Illustration of a navy fish swimming left"/>

  <!-- Headline -->
  <g class="headline display">
    <text class="navy" x="205" y="835" font-size="250" textLength="1125" lengthAdjust="spacingAndGlyphs">GOLDEN CRUST</text>
    <text class="red" x="205" y="1180" font-size="436" textLength="1125" lengthAdjust="spacingAndGlyphs">SUPPER</text>
    <text class="navy" x="205" y="1307" font-size="136" textLength="1125" lengthAdjust="spacingAndGlyphs">ALL-YOU-CAN-EAT FISH FRY</text>
  </g>

  <!-- Admission -->
  <g class="admission display">
    <polygon class="red" points="230,1360 622,1360 567,1468 185,1468"/>
    <text class="white" x="240" y="1445" font-size="100" textLength="325" lengthAdjust="spacingAndGlyphs">ADMISSION:</text>
    <polygon class="navy" points="655,1352 1352,1352 1265,1474 562,1474"/>
    <text class="white" x="657" y="1405" font-size="60" textLength="642" lengthAdjust="spacingAndGlyphs">DONATION OF ANY BASEBALL EQUIPMENT</text>
    <text class="white" x="634" y="1457" font-size="60" textLength="462" lengthAdjust="spacingAndGlyphs">OR FINANCIAL CONTRIBUTION</text>
    <line x1="1108" y1="1440" x2="1290" y2="1440" stroke="var(--white)" stroke-width="4"/>
  </g>

  <!-- Donation items band -->
  <g class="donation-items display">
    <rect class="red" x="131" y="1508" width="1276" height="92"/>
    <text class="white" x="179" y="1576" font-size="64" textLength="81" lengthAdjust="spacingAndGlyphs">BATS</text>
    <text class="white" x="293" y="1576" font-size="64" textLength="129" lengthAdjust="spacingAndGlyphs">GLOVES</text>
    <text class="white" x="455" y="1576" font-size="64" textLength="141" lengthAdjust="spacingAndGlyphs">JERSEYS</text>
    <text class="white" x="629" y="1576" font-size="64" textLength="121" lengthAdjust="spacingAndGlyphs">CLEATS</text>
    <text class="white" x="784" y="1576" font-size="64" textLength="102" lengthAdjust="spacingAndGlyphs">BALLS</text>
    <text class="white" x="920" y="1576" font-size="64" textLength="437" lengthAdjust="spacingAndGlyphs">FINANCIAL CONTRIBUTION</text>
    <g stroke="var(--white)" stroke-width="3">
      <line x1="276" y1="1528" x2="276" y2="1582"/>
      <line x1="437" y1="1528" x2="437" y2="1582"/>
      <line x1="611" y1="1528" x2="611" y2="1582"/>
      <line x1="767" y1="1528" x2="767" y2="1582"/>
      <line x1="903" y1="1528" x2="903" y2="1582"/>
    </g>
  </g>

  <!-- Flags -->
  <g class="flag flag-left">
    <rect class="navy" x="178" y="1636" width="57" height="40"/>
    <rect class="red" x="259" y="1636" width="57" height="40"/>
    <rect class="red" x="178" y="1700" width="57" height="40"/>
    <rect class="navy" x="259" y="1700" width="57" height="40"/>
  </g>
  <g class="flag flag-right">
    <rect class="navy" x="1222" y="1636" width="57" height="40"/>
    <rect class="red" x="1303" y="1636" width="57" height="40"/>
    <rect class="red" x="1222" y="1700" width="57" height="40"/>
    <rect class="navy" x="1303" y="1700" width="57" height="40"/>
  </g>

  <!-- Event details -->
  <g class="event-details body-text">
    <text x="338" y="1678" font-size="48" textLength="860" lengthAdjust="spacingAndGlyphs"><tspan class="navy">Date &amp; Time: </tspan><tspan class="red" font-weight="700">May 17th, 6 PM – 10 PM</tspan></text>
    <g class="pin-icon red">
      <path d="M362,1694 a12,12 0 0 1 12,12 c0,9 -12,20 -12,20 c0,0 -12,-11 -12,-20 a12,12 0 0 1 12,-12 z M362,1701 a5,5 0 1 0 0.01,0 z" fill-rule="evenodd"/>
      <polygon points="345,1722 353,1722 362,1730 371,1722 379,1722 384,1736 340,1736"/>
    </g>
    <text class="navy" x="400" y="1733" font-size="48" textLength="798" lengthAdjust="spacingAndGlyphs">4721 Quillon Ln. Mansfield, TX 76048</text>
  </g>
</svg>
</body>
</html>
```